Copper Lantern Vitamin and Supplements site

I would like a design for vitamin and supplements website that will only stock the very best products. These vitamins will expensive. It needs to look distinct from the various vitamin, health and beauty websites. It needs to be simple and elegant, unisex, and with a mild/slight scientific feel. I will be choosing my products that are sold on my site based on great reviews and the tested science behind the products. This rigour should be reflected in the look and feel of the site.

I have a separate project for the coding the website, however I need further ideas on the design itself.

This site is for people who are willing to try new things and care deeply about their health.

Health And Wellness

```html
<!DOCTYPE html>
<html lang="en">
<head>
<meta charset="utf-8">
<title>Copper Lantern — Supplements</title>
<link rel="stylesheet" href="https://fonts.googleapis.com/css2?family=Poppins:ital,wght@0,400;0,500;0,600;0,700;1,400&display=swap">
<style>
:root{
  --green:#2ec52e;
  --ink:#2b2838;
  --body:#5d5b66;
  --band:#f4f4f5;
  --line:#ececec;
  --check:#263b33;
}
*{box-sizing:border-box;margin:0;padding:0}
html,body{width:770px;height:1200px;overflow:hidden;background:#fff}
body{position:relative;font-family:"Poppins",sans-serif;color:var(--ink)}
.abs{position:absolute}
.btn{position:absolute;display:flex;align-items:center;justify-content:center;border-radius:12px;font-size:6.5px;font-weight:700;text-transform:uppercase;letter-spacing:-.1px}
.btn-solid{background:var(--green);color:#fff}
.btn-ghost{border:1px solid var(--green);color:var(--green);background:#fff}

/* header */
.site-header{position:absolute;left:0;top:0;width:770px;height:47px;border-bottom:1px solid #eef5ee}
.brand{position:absolute;left:48px;top:14px;display:flex;align-items:center;gap:5px;font-size:13px;font-weight:500;color:var(--ink)}
.brand-dot{width:10px;height:10px;border-radius:50%;background:var(--green)}
.nav{position:absolute;left:228px;top:17px;display:flex;gap:14px;font-size:7px;font-weight:500;color:var(--ink)}
.nav-icons{position:absolute;left:503px;top:16px;display:flex;gap:10px;align-items:center}

/* hero */
.hero-title{left:50px;top:134px;font-size:30px;font-weight:700;line-height:35px;letter-spacing:-1px}
.hero-title em{font-style:normal;color:var(--green)}
.hero-text{left:50px;top:211px;width:260px;font-size:7.5px;line-height:13.5px;color:var(--body)}
.hero-visual{left:340px;top:108px;width:274px;height:215px;border-radius:40px 40px 30px 30px;background:radial-gradient(ellipse at 50% 45%,#2c3a4a 0%,#17191d 55%,#0c0d0f 100%)}

/* features */
.features{left:0;top:384px;width:761px;height:124px;background:var(--band)}
.feature{position:absolute;top:0;width:120px;text-align:center}
.feature-icon{width:44px;height:44px;border-radius:50%;background:#fff;margin:6px auto 0;box-shadow:0 1px 3px rgba(0,0,0,.06);display:flex;align-items:center;justify-content:center}
.feature-icon span{width:22px;height:22px;border-radius:6px;background:linear-gradient(135deg,#e84a3f,#f6a542)}
.feature h3{margin-top:11px;font-size:8px;font-weight:600}
.feature p{margin-top:5px;font-size:6.4px;line-height:12px;color:var(--body)}

/* about */
.about-visual{left:83px;top:557px;width:248px;height:258px;border-radius:30px 30px 40px 40px;background:linear-gradient(180deg,#1a1a1a 0%,#1a1a1a 10%,#63b43c 12%,#6fbd42 60%,#2f5a1c 100%)}
.eyebrow{left:361px;top:565px;font-size:5.5px;font-weight:700;letter-spacing:1.6px;color:var(--green)}
.about-title{left:361px;top:577px;font-size:16.5px;font-weight:700;line-height:23px}
.about-text{left:361px;top:636px;width:215px;font-size:6.5px;line-height:11.8px;font-style:italic;color:var(--body)}
.checks{left:361px;top:687px;list-style:none}
.checks li{display:flex;align-items:center;gap:7px;height:21.4px;font-size:6.5px;font-weight:500;color:var(--ink)}
.checks li svg{flex:none}

/* product */
.product-visual{left:46px;top:834px;width:313px;height:284px;background:#f3f3f3}
.product-jar{left:129px;top:878px;width:146px;height:198px;border-radius:18px 18px 28px 28px;background:linear-gradient(180deg,#1b1b1b 0%,#1b1b1b 10%,#f08d1c 13%,#f08a16 75%,#1b1b1b 100%)}
.thumb{top:1128px;width:72px;height:59px;background:#f3f3f3}
.thumb i{position:absolute;left:50%;top:8px;width:22px;height:45px;margin-left:-11px;border-radius:5px}
.product-name{left:384px;top:844px;font-size:13px;font-weight:600;text-transform:uppercase}
.price{left:384px;top:868px;font-size:10px;font-weight:500;color:var(--green);display:flex;align-items:center;gap:9px}
.product-text{left:384px;top:896px;width:232px;font-size:6.5px;line-height:11.8px;color:var(--body)}
.divider{left:384px;top:992px;width:231px;border-top:1px dashed #ddd}
.info-label{left:384px;top:1007px;font-size:6.5px;font-weight:600;text-transform:uppercase}
.category{left:384px;top:1025px;font-size:6.3px;text-transform:uppercase;color:var(--body)}
.category b{color:var(--green);font-weight:600;margin-right:3px}
.tabs{left:384px;top:1066px;display:flex;gap:13px;font-size:6.8px;font-weight:600;text-transform:uppercase}
.tabs .active{border-bottom:1.5px solid var(--green);padding-bottom:3px}
.tab-text{left:384px;top:1090px;width:232px;font-size:6.3px;line-height:11.8px;color:var(--body)}
</style>
</head>
<body>

<header class="site-header">
  <div class="brand"><span class="brand-dot"></span>Copper Lantern</div>
  <nav class="nav"><span>Home</span><span>Supplement</span><span>Order</span><span>Price</span><span>Ingredient</span><span>Blog</span><span>Contact</span></nav>
  <div class="nav-icons">
    <svg width="8" height="8" viewBox="0 0 10 10"><circle cx="4" cy="4" r="3" fill="none" stroke="#2ec52e" stroke-width="1.5"/><path d="M6.3 6.3L9 9" stroke="#2ec52e" stroke-width="1.5"/></svg>
    <svg width="9" height="9" viewBox="0 0 10 10"><path d="M1 3h8l-1 5H2z" fill="#2ec52e"/></svg>
  </div>
  <a class="btn btn-solid" style="left:546px;top:11px;width:76px;height:22px">Order now</a>
</header>

<h1 class="abs hero-title">Super <em>Convenient</em><br>Quality Protein</h1>
<p class="abs hero-text">Lorem ipsum dolor sit amet, consectetur seddo eiumod tempor incididunt labore adipiscing seddo eiumod</p>
<a class="btn btn-solid" style="left:50px;top:254px;width:72px;height:23px">Purchase</a>
<a class="btn btn-ghost" style="left:132px;top:254px;width:70px;height:23px">Contact</a>
<div class="abs hero-visual" role="img" aria-label="Three dark supplement tubs with coloured labels"></div>

<section class="abs features">
  <div class="feature" style="left:49px"><div class="feature-icon"><span></span></div><h3>Increased Energy</h3><p>Lorem ipsum dolor sitamet molis<br>region dolor amet mis.</p></div>
  <div class="feature" style="left:196px"><div class="feature-icon"><span></span></div><h3>Calorie Build Up</h3><p>Lorem ipsum dolor sitamet molis<br>region dolor amet mis.</p></div>
  <div class="feature" style="left:343px"><div class="feature-icon"><span></span></div><h3>Energy Grow Up</h3><p>Lorem ipsum dolor sitamet molis<br>region dolor amet mis.</p></div>
  <div class="feature" style="left:490px"><div class="feature-icon"><span></span></div><h3>Regular Routine</h3><p>Lorem ipsum dolor sitamet molis<br>region dolor amet mis.</p></div>
</section>

<div class="abs about-visual" role="img" aria-label="Green supplement tub, salted caramel flavour"></div>
<p class="abs eyebrow">ABOUT SUPPLEMENT</p>
<h2 class="abs about-title">Dietary Supplement Pill<br>Product Intended</h2>
<p class="abs about-text">Lorem ipsum, or lipsum as it is sometimes known dummy text used in laying out print, graphic or web designs. The passage is attributed to an unknown.</p>
<ul class="abs checks">
  <li><svg width="15" height="15" viewBox="0 0 16 16"><circle cx="8" cy="8" r="8" fill="#263b33"/><path d="M5 8.2l2 2 4-4" fill="none" stroke="#2ec52e" stroke-width="1.5"/></svg>Sometimes known dummy</li>
  <li><svg width="15" height="15" viewBox="0 0 16 16"><circle cx="8" cy="8" r="8" fill="#263b33"/><path d="M5 8.2l2 2 4-4" fill="none" stroke="#2ec52e" stroke-width="1.5"/></svg>Best solution for developing your business</li>
  <li><svg width="15" height="15" viewBox="0 0 16 16"><circle cx="8" cy="8" r="8" fill="#263b33"/><path d="M5 8.2l2 2 4-4" fill="none" stroke="#2ec52e" stroke-width="1.5"/></svg>Deserunt ad ipsum sint excepteur</li>
  <li><svg width="15" height="15" viewBox="0 0 16 16"><circle cx="8" cy="8" r="8" fill="#263b33"/><path d="M5 8.2l2 2 4-4" fill="none" stroke="#2ec52e" stroke-width="1.5"/></svg>Lorem sit occaecat ea proident excepteur</li>
</ul>
<a class="btn btn-solid" style="left:361px;top:786px;width:68px;height:22px">Buy now</a>

<div class="abs product-visual"></div>
<div class="abs product-jar" role="img" aria-label="Orange supplement tub, salted caramel flavour"></div>
<div class="abs thumb" style="left:46px"><i style="background:#f08a16;width:34px;margin-left:-17px"></i></div>
<div class="abs thumb" style="left:126px"><i style="background:#6fcf2e"></i></div>
<div class="abs thumb" style="left:207px"><i style="background:#e0242b"></i></div>
<div class="abs thumb" style="left:288px"><i style="background:#2fbfe6"></i></div>

<h2 class="abs product-name">Lumen Capsule</h2>
<div class="abs price">£120.00
  <svg width="29" height="6" viewBox="0 0 50 10" fill="#2ec52e"><g id="s"><path d="M5 0l1.5 3.2 3.5.4-2.6 2.4.7 3.5L5 7.8 1.9 9.5l.7-3.5L0 3.6l3.5-.4z"/></g><use href="#s" x="10"/><use href="#s" x="20"/><use href="#s" x="30"/><use href="#s" x="40"/></svg>
</div>
<p class="abs product-text">There are many variations of passages of Lorem Ipsum available, but the majority have suffered alteration in some form, by injected humour, or randomised words which even slightly believable.</p>
<a class="btn btn-solid" style="left:384px;top:951px;width:76px;height:22px">Order now</a>
<div class="abs divider"></div>
<p class="abs info-label">Product info</p>
<p class="abs category"><b>Category:</b>Lumen Cap</p>
<div class="abs tabs"><span class="active">Description</span><span>Reviews (1)</span></div>
<p class="abs tab-text">Pellentesque habitant morbi tristique senectus et netus et malesuada fames ac turpis egestas. Vestibulum tortor quam, feugiat vitae, ultricies eget, tempor sit amet, ante. Donec eu libero sit amet quam egestas semper. Aenean ultricies mi vitae est. Mauris placerat eleifend leo.</p>

</body>
</html>
```